Stationary for I.T. company
DuskVale
Stationary for I.T. company - Information Technology
Creative Brief
Bright & Fun-filled
Ray Olsen
Director
PO Box 4172 Marlow ACT 2913
ops@duskva.le
duskva.le
Eye catching - display the DuskVale logo with either the red N with the white text or the white only logo on a background with either bold colours, dark greys or black. Open to other concepts or suggestions if they are eye catching
brimlow brimlow
Thank you everyone for your efforts. We may ask a couple more questons to relevant designers - but we plan to decide in the next 24 to 48 hours. Thanks again.
Thanks everyone for your submissions so far.. 266 designs is much much more than we were expecting. To help everyone understand where we are going and what we are looking for we will start eliminating some designs tonight. With that, we will probably start to give out a couple (maybe 3) 5 star ratings. These will indicate the current leading designs. We will probably also redo most of the star ratings out there to better give designers a better understanding of what we like. Please note that there is several people looking at these designs, so star rating may go up and down a little... but be assured if it has stars, we like it, or like some concepts in it.
We will aim to provide every designer feedback and stars (so yes - it may look like we rate a lot of things highly). 4 stars will generally be used to indicate the favorite submission of a designer, and 5 will only be used when we start eliminating designs.
tallfern tallfern
Check your private messages...
Also looking for letter head, invoice, envelope, notepad templates, presentation folder in addition to business card design. Thanks.
Amendment to the design brief - we will also accept a white background for the back of the business card

```html
<!DOCTYPE html>
<html lang="en">
<head>
<meta charset="UTF-8">
<title>DuskVale Business Card</title>
<link href="https://fonts.googleapis.com/css2?family=Open+Sans:wght@400;600;700;800&display=swap" rel="stylesheet">
<style>
  :root {
    --backdrop: #e8e8ea;
    --red: #e3141d;
    --red-deep: #b00a12;
    --red-light: #f0474d;
    --white: #ffffff;
    --ink: #3a3a3c;
    --ink-soft: #8a8a8e;
    --shadow: rgba(0,0,0,0.18);
  }
  * { margin: 0; padding: 0; box-sizing: border-box; }
  html, body {
    width: 1200px; height: 961px; overflow: hidden;
    background: var(--backdrop);
    font-family: "Open Sans", Arial, sans-serif;
  }
  .stage { position: relative; width: 1200px; height: 961px; }

  .card {
    position: absolute;
    width: 500px; height: 286px;
    border-radius: 24px;
    overflow: hidden;
    box-shadow: 0 14px 30px var(--shadow);
  }

  /* Front */
  .card--front {
    left: 90px; top: 230px;
    background: linear-gradient(135deg, var(--red) 0%, var(--red-deep) 100%);
  }
  .front-glow {
    position: absolute; inset: 0;
    background: radial-gradient(ellipse at 45% 40%, rgba(255,255,255,0.14) 0%, rgba(255,255,255,0) 60%);
  }
  .front-brand {
    position: absolute; left: 0; right: 0; top: 112px;
    display: flex; align-items: center; justify-content: center; gap: 10px;
  }
  .brand-dot { width: 30px; height: 30px; border-radius: 50%; flex: none; }
  .card--front .brand-dot { background: var(--white); }
  .brand-name { font-weight: 800; font-size: 27px; letter-spacing: -0.5px; }
  .card--front .brand-name { color: var(--white); }
  .front-web {
    position: absolute; left: 0; right: 0; top: 160px; text-align: center;
    color: rgba(255,255,255,0.75); font-size: 9px; letter-spacing: 6px;
  }

  /* Back */
  .card--back {
    left: 620px; top: 430px;
    background: var(--white);
  }
  .back-art {
    position: absolute; right: 0; top: 76px; bottom: 0; width: 250px;
    background: linear-gradient(135deg, var(--red-light) 0%, var(--red) 45%, var(--red-deep) 100%);
  }
  .back-brand {
    position: absolute; left: 26px; top: 104px;
    display: flex; align-items: center; gap: 8px;
  }
  .card--back .brand-dot { background: var(--red); width: 34px; height: 34px; }
  .card--back .brand-name { color: var(--ink); font-size: 28px; }
  .person {
    position: absolute; right: 54px; top: 34px; text-align: right;
  }
  .person-name { color: var(--red); font-weight: 700; font-size: 14px; }
  .person-title { color: var(--ink-soft); font-size: 7px; margin-top: 1px; }
  .contact {
    position: absolute; left: 42px; top: 160px; list-style: none;
  }
  .contact li {
    display: flex; align-items: center; gap: 7px;
    color: var(--ink); font-size: 8.5px; line-height: 13.5px;
  }
  .contact svg { width: 8px; height: 8px; fill: var(--red); flex: none; }
  .contact .no-icon { width: 8px; flex: none; }
</style>
</head>
<body>
<main class="stage">

  <section class="card card--front">
    <div class="front-glow"></div>
    <div class="front-brand">
      <span class="brand-dot"></span>
      <span class="brand-name">DuskVale</span>
    </div>
    <p class="front-web">www.duskva.le</p>
  </section>

  <section class="card card--back">
    <div class="back-art" role="img" aria-label="Red and white brand illustration area"></div>
    <div class="person">
      <p class="person-name">Ray Olsen</p>
      <p class="person-title">Director</p>
    </div>
    <div class="back-brand">
      <span class="brand-dot"></span>
      <span class="brand-name">DuskVale</span>
    </div>
    <ul class="contact">
      <li><svg viewBox="0 0 10 10"><path d="M5 0a3.5 3.5 0 0 0-3.5 3.5C1.5 6 5 10 5 10s3.5-4 3.5-6.5A3.5 3.5 0 0 0 5 0zm0 5a1.5 1.5 0 1 1 0-3 1.5 1.5 0 0 1 0 3z"/></svg>PO Box 4172</li>
      <li><span class="no-icon"></span>Marlow ACT 2913</li>
      <li><svg viewBox="0 0 10 10"><path d="M2 0l2 2.5-1 1.3a6 6 0 0 0 3.2 3.2l1.3-1L10 8l-1.5 2C4 10 0 6 0 1.5z"/></svg>(02) 6255 0148</li>
      <li><svg viewBox="0 0 10 10"><rect x="2.5" y="0" width="5" height="10" rx="1"/></svg>0412 660 395</li>
      <li><svg viewBox="0 0 10 10"><path d="M0 2h10v6H0zM0 2l5 3.5L10 2" stroke="#fff" stroke-width="0.8"/></svg>ops@duskva.le</li>
      <li><svg viewBox="0 0 10 10"><circle cx="5" cy="5" r="5"/></svg>www.duskva.le</li>
    </ul>
  </section>

</main>
</body>
</html>
```